Web SITE design for new book

I need a unique design for a book my friend is releasing.

The home page needs to include:
A picture of the book
A spot for a video

Navigation:
Home
About the Book
Buy the Book
About the Author
Investing
Log In

The person awarded the project will also need to provide designs for the 5 other internal pages. They should be pretty straight forward.

Link to book design: https://www.filvantra.net/s/qmrt82kw7zpalvq/book-cover.png

Thanks!

```html
<!DOCTYPE html>
<html lang="en">
<head>
<meta charset="utf-8">
<title>Page Debut – New Book</title>
<link href="https://fonts.googleapis.com/css2?family=Raleway:ital,wght@0,300;0,400;0,500;0,600;0,700;1,400&display=swap" rel="stylesheet">
<style>
:root{
  --gold:#9b8232;
  --gold-dark:#8a7329;
  --ink:#333333;
  --muted:#9a9a9a;
  --body:#7d7d7d;
  --line:#e2e2e2;
  --band:#ececec;
  --foot:#2c2c2c;
  --foot-deep:#232323;
  --foot-text:#bdbdbd;
  --white:#ffffff;
}
*{box-sizing:border-box;margin:0;padding:0}
html,body{width:1200px;height:2609px;overflow:hidden;background:var(--white)}
body{position:relative;font-family:'Raleway',sans-serif;color:var(--ink)}
.abs{position:absolute}

/* header */
.site-header{left:0;top:0;width:1200px;height:121px;border-bottom:1px solid var(--line)}
.brand{left:78px;top:40px;font-size:30px;font-weight:700;letter-spacing:.5px;color:var(--gold)}
.brand span{color:var(--gold)}
.search{left:866px;top:21px;width:263px;height:31px;border:1px solid #cfcfcf;border-radius:4px;background:linear-gradient(#fafafa,#ececec)}
.search p{position:absolute;left:10px;top:7px;font-size:12px;color:#bbb}
.search svg{position:absolute;right:7px;top:7px}
.nav{left:466px;top:87px;display:flex;gap:0;font-size:14px;font-weight:500;color:#444}
.nav a{color:inherit;text-decoration:none;position:absolute;white-space:nowrap}
.nav .current{color:var(--gold)}
.nav-underline{left:465px;top:116px;width:43px;height:4px;background:var(--gold)}

/* hero */
.hero{left:0;top:122px;width:1200px;height:480px;background:linear-gradient(#d4d4d4 0%,#e9e9e9 55%,#ffffff 100%);box-shadow:0 3px 6px rgba(0,0,0,.08)}
.hero-arrow{width:38px;height:38px;border-radius:50%;background:var(--white);top:305px}
.hero-arrow svg{position:absolute;left:11px;top:11px}
.hero-title{left:177px;top:282px;font-size:33px;font-weight:400;color:#3a3a3a}
.hero-text{left:180px;top:333px;width:460px;font-size:14px;line-height:26px;color:#888}
.btn{background:var(--gold);color:var(--white);font-size:17px;font-weight:500;text-align:center}
.hero-btn{left:489px;top:445px;width:145px;height:53px;line-height:53px}
.book-cover{left:713px;top:165px;width:260px;height:385px;background:linear-gradient(135deg,#ffffff 0%,#f1f1f1 60%,#d9d9d9 100%);box-shadow:8px 14px 24px rgba(0,0,0,.25);border-left:6px solid #cfcfcf}

/* about the book */
.section-title{left:0;width:1200px;text-align:center;font-size:38px;font-weight:300;color:#2f2f2f}
.book-text{left:118px;top:732px;width:970px;text-align:center;font-size:16px;line-height:28px;color:var(--muted)}
.video{left:269px;top:896px;width:662px;height:286px;background:radial-gradient(ellipse at 55% 40%,#4a3b36 0%,#2a2422 55%,#1a1716 100%)}
.play{left:571px;top:1009px}

/* author */
.author-band{left:0;top:1238px;width:1200px;height:452px;background:var(--band)}
.author-photo{left:78px;top:1359px;width:300px;height:214px;border:3px solid var(--white);background:linear-gradient(160deg,#c9c27a 0%,#b9a57a 45%,#8c8d95 100%)}
.author-name{left:78px;top:1594px;width:250px;text-align:center;font-size:17px;font-weight:500;color:var(--gold)}
.author-text{left:412px;top:1357px;width:700px;font-size:16px;line-height:31px;color:#999}
.author-btn{left:412px;top:1591px;width:146px;height:54px;line-height:54px}

/* testimonials */
.quote{width:420px;height:130px}
.avatar{position:absolute;left:0;top:0;width:114px;height:114px;border-radius:50%;border:4px solid var(--white);box-shadow:0 0 0 1px #ddd,0 2px 5px rgba(0,0,0,.2)}
.quote-text{position:absolute;left:132px;top:8px;width:270px;font-size:14px;font-style:italic;line-height:19px;color:#888}
.quote-text b{font-size:22px;font-weight:400;font-style:normal;color:#aaa;line-height:0}
.quote-by{position:absolute;left:136px;top:112px;font-size:15px;font-style:italic;color:#333}

/* footer */
.site-footer{left:0;top:2242px;width:1200px;height:367px;background:var(--foot)}
.foot-head{top:2279px;font-size:15px;font-weight:600;color:var(--gold)}
.foot-list{left:80px;top:2326px;list-style:none;font-size:12px;line-height:25px;color:#ddd;font-weight:500}
.foot-list li::before{content:"›";margin-right:8px;color:#aaa}
.news{left:321px;width:245px;font-size:15px;line-height:20px;color:#ddd}
.news small{display:block;font-size:12px;color:#999;margin-top:2px}
.news-rule{left:321px;top:2400px;width:245px;border-top:1px dashed #555}
.newsletter-text{left:649px;top:2322px;width:245px;font-size:15px;line-height:20px;color:#ccc}
.email-field{left:651px;top:2380px;width:229px;height:30px;background:#5a5a5a;border:1px solid #6a6a6a;font-size:12px;color:#bbb;padding:7px 10px}
.subscribe{left:652px;top:2424px;width:114px;height:36px;line-height:36px;font-size:13px;font-weight:700}
.contact{left:955px;font-size:13px;color:#ddd;display:flex;align-items:center;gap:10px}
.social{top:2422px;width:38px;height:38px;border-radius:50%;background:#8a8a8a;border:2px solid #a5a5a5}
.foot-bottom{left:0;top:2524px;width:1200px;height:85px;background:var(--foot-deep)}
.foot-brand{left:78px;top:2553px;font-size:23px;font-weight:700;color:#555}
.copyright{left:450px;top:2562px;font-size:12px;color:#999}
</style>
</head>
<body>

<header class="abs site-header"></header>
<div class="abs brand">PAGE DEBUT</div>
<div class="abs search">
  <p>Search</p>
  <svg width="17" height="17" viewBox="0 0 17 17"><circle cx="7" cy="7" r="5" fill="none" stroke="#222" stroke-width="2.4"/><line x1="10.5" y1="10.5" x2="15.5" y2="15.5" stroke="#222" stroke-width="3" stroke-linecap="round"/></svg>
</div>
<nav class="abs nav">
  <a class="current" style="left:0">HOME</a>
  <a style="left:70px">ABOUT THE BOOK</a>
  <a style="left:220px">BUY THE BOOK</a>
  <a style="left:348px">ABOUT THE AUTHOR</a>
  <a style="left:514px">INVESTING</a>
  <a style="left:617px">LOG IN</a>
</nav>
<div class="abs nav-underline"></div>

<section class="abs hero"></section>
<div class="abs hero-arrow" style="left:39px"><svg width="16" height="16" viewBox="0 0 16 16"><path d="M10 2 L4 8 L10 14" fill="none" stroke="#888" stroke-width="3"/></svg></div>
<div class="abs hero-arrow" style="left:1128px"><svg width="16" height="16" viewBox="0 0 16 16"><path d="M6 2 L12 8 L6 14" fill="none" stroke="#888" stroke-width="3"/></svg></div>
<h1 class="abs hero-title">Vivamus elementum semper</h1>
<p class="abs hero-text">Sed ut perspiciatis unde omnis iste natus error sit voluptatem accusantium doloremque laudantium, totam rem aperiam, eaque ipsa quae ab illo inventore veritatis et quasi architecto beatae vitae dicta sunt explicabo.</p>
<div class="abs btn hero-btn">BUY NOW</div>
<div class="abs book-cover" role="img" aria-label="Book cover of the new investing book, white cover with gold title"></div>

<h2 class="abs section-title" style="top:662px">About the Book</h2>
<p class="abs book-text">Sed ut perspiciatis unde omnis iste natus error sit voluptatem accusantium doloremque laudantium, totam rem aperiam, eaque ipsa quae ab illo inventore veritatis et quasi architecto beatae vitae dicta sunt explicabo. Nemo enim ipsam voluptatem quia voluptas Sed ut perspiciatis unde omnis iste natus error sit voluptatem accusantium doloremque laudantium, totam rem aperiam, eaque ipsa quae ab illo inventore veritatis et quasi architecto beatae vitae dicta sunt explicabo. Nemo enim ipsam voluptatem quia voluptas</p>
<div class="abs video" role="img" aria-label="Video still of a family reading a book together"></div>
<svg class="abs play" width="58" height="58" viewBox="0 0 58 58"><circle cx="29" cy="29" r="26" fill="#111" stroke="#fff" stroke-width="3"/><path d="M23 17 L41 29 L23 41 Z" fill="#fff"/></svg>

<section class="abs author-band"></section>
<h2 class="abs section-title" style="top:1268px">About the Author</h2>
<div class="abs author-photo" role="img" aria-label="Portrait photo of the author outdoors"></div>
<div class="abs author-name">M ORLEN VALE</div>
<p class="abs author-text">Sed ut perspiciatis unde omnis iste natus error sit voluptatem accusantium doloremque laudantium, totam rem aperiam, eaque ipsa quae ab illo inventore veritatis et quasi architecto beatae vitae dicta sunt explicabo. Nemo enim ipsam voluptatem quia voluptas Sed ut perspiciatis unde omnis iste natus error sit voluptatem accusantium doloremque laudantium, totam rem aperiam, eaque ipsa quae ab illo inventore veritatis et quasi architecto beatae vitae dicta sunt explicabo. Nemo enim ipsam voluptatem quia voluptasNemo enim ipsam voluptatem quia voluptas</p>
<div class="abs btn author-btn">KNOW MORE</div>

<h2 class="abs section-title" style="top:1748px">What Our Customer Says</h2>

<div class="abs quote" style="left:133px;top:1850px">
  <div class="avatar" role="img" aria-label="Customer portrait" style="background:linear-gradient(#e8c9a6,#c98a64)"></div>
  <p class="quote-text"><b>“</b>Nemo enim ipsam voluptatem quia voluptas Sed ut perspiciatis unde omnis iste natus error sit voluptatem accusantium doloremque laudantium, totam rem aperiam. <b>”</b></p>
  <p class="quote-by">- Customer Name</p>
</div>
<div class="abs quote" style="left:646px;top:1850px">
  <div class="avatar" role="img" aria-label="Customer portrait" style="background:linear-gradient(#8a6a4a,#c4743e)"></div>
  <p class="quote-text"><b>“</b>Nemo enim ipsam voluptatem quia voluptas Sed ut perspiciatis unde omnis iste natus error sit voluptatem accusantium doloremque laudantium, totam rem aperiam. <b>”</b></p>
  <p class="quote-by">- Customer Name</p>
</div>
<div class="abs quote" style="left:133px;top:2039px">
  <div class="avatar" role="img" aria-label="Customer portrait" style="background:linear-gradient(#a0482a,#e0a57a)"></div>
  <p class="quote-text"><b>“</b>Nemo enim ipsam voluptatem quia voluptas Sed ut perspiciatis unde omnis iste natus error sit voluptatem accusantium doloremque laudantium, totam rem aperiam. <b>”</b></p>
  <p class="quote-by">- Customer Name</p>
</div>
<div class="abs quote" style="left:646px;top:2039px">
  <div class="avatar" role="img" aria-label="Customer portrait" style="background:linear-gradient(#8fa3b8,#e2b896)"></div>
  <p class="quote-text"><b>“</b>Nemo enim ipsam voluptatem quia voluptas Sed ut perspiciatis unde omnis iste natus error sit voluptatem accusantium doloremque laudantium, totam rem aperiam. <b>”</b></p>
  <p class="quote-by">- Customer Name</p>
</div>

<footer class="abs site-footer"></footer>
<div class="abs foot-head" style="left:80px">QUICK LINKS</div>
<div class="abs foot-head" style="left:321px">LATEST NEWS</div>
<div class="abs foot-head" style="left:649px">NEWSLETTER SIGNUP</div>
<div class="abs foot-head" style="left:955px">REACH US</div>
<ul class="abs foot-list">
  <li>ABOUT THE BOOK</li><li>BUY THE BOOK</li><li>ABOUT THE AUTHOR</li><li>INVESTING</li><li>LOG IN</li>
</ul>
<p class="abs news" style="top:2322px">Nemo enim ipsam voluptatem quia voluptas Nemo enim<small>25 Mar 2014</small></p>
<div class="abs news-rule"></div>
<p class="abs news" style="top:2411px">Nemo enim ipsam voluptatem quia voluptas Nemo enim<small>25 Mar 2014</small></p>
<p class="abs newsletter-text">Subscribe our newsletter to know our daily updates and offer.</p>
<div class="abs email-field">Enter your Email Id</div>
<div class="abs btn subscribe">SUBSCRIBE</div>
<div class="abs contact" style="top:2326px"><svg width="17" height="17" viewBox="0 0 24 24"><path d="M6.6 10.8a15 15 0 0 0 6.6 6.6l2.2-2.2c.3-.3.7-.4 1-.2 1.1.4 2.3.6 3.6.6.6 0 1 .4 1 1V20c0 .6-.4 1-1 1C10.6 21 3 13.4 3 4c0-.6.4-1 1-1h3.5c.6 0 1 .4 1 1 0 1.3.2 2.5.6 3.6.1.3 0 .7-.2 1z" fill="#bbb"/></svg>(555) - 014-2370</div>
<div class="abs contact" style="top:2364px"><svg width="16" height="12" viewBox="0 0 16 12"><rect width="16" height="12" fill="#bbb"/><path d="M0 0 L8 7 L16 0" fill="none" stroke="#2c2c2c" stroke-width="1.5"/></svg>info@pagedebut.com</div>
<div class="abs social" style="left:955px"></div>
<div class="abs social" style="left:997px"></div>
<div class="abs social" style="left:1038px"></div>
<div class="abs social" style="left:1080px"></div>
<div class="abs foot-bottom"></div>
<div class="abs foot-brand">PAGE DEBUT</div>
<div class="abs copyright">All Rights Reserved. Copyrights @ 2014</div>

</body>
</html>
```